Yoga Training Cerificate

Design a certificate of graduation from a Vinyasa Yoga Teacher Training Program.

The attached document is an example of the certificate I received as a graduate from a teacher training program. You can use it as a template.

Stylistically, what you design can be: visually enticing, professional, clean, and modern.

Please develop the "Lumen Stretch" logo and embed it within the certificate.

Please add a circular watermark behind the body of the certificate similar to the one found in the attachment; leave out the words Asana Guildhall because I am not associated with that organization.

The name of my school is "Lumen Stretch." And it was established in 2017, which you can include.

The certificate affirms that "' 'such-and-such' has successfully completed the Lumen Stretch modern vinyasa yoga training, completing two hundred hours of instruction in practice and theory. Within the power of our institution as a certifying agent we declare Such-and-such, now, a teacher competent to share the gift of yoga with the masses in a safe and effective."

My name -Dennis Whitcombe- should be at bottom with a faux-signature; position title: Lumen Stretch founder.

If you decide to include text on the fringe, like the example, it might include bars of text describing the maxims of the Lumen Stretch school reading:

This is Lumen Stretch
Breath is primary
Evolve the physical culture
Bring your unique expression to the practice
Take Breaks
Freestyle
Close your eyes
Feel deeper into your body
This is active meditation
This is moving meditation
This is modern meditation

And find a way to integrate Emojis like: Fire, Water, Prayer Hands, etc. as you see fit.

Generally, make the certificate look: official, clear and clean. You can base it from the example given. And try and create a graphic design that is more visually capturing then the example.

```html
<!DOCTYPE html>
<html lang="en">
<head>
<meta charset="utf-8">
<title>Lumen Stretch — Certification of Completion</title>
<link rel="stylesheet" href="https://fonts.googleapis.com/css2?family=Cormorant+Garamond:ital,wght@1,500;1,600&family=EB+Garamond:ital,wght@1,400;1,700&family=Cutive+Mono&family=Montserrat:wght@500&family=Petit+Formal+Script&display=swap">
<style>
  :root {
    --paper: #ffffff;
    --ink: #1a1a1a;
    --ink-soft: #333333;
    --maxim-grey: #8a8a8a;
    --brand-grey: #6e6e6e;
    --icon-grey: #7a7a7a;
    --seal-grey: #ebebeb;
    --rule: #555555;
  }
  * { margin: 0; padding: 0; box-sizing: border-box; }
  html, body { width: 1200px; height: 943px; overflow: hidden; background: var(--paper); }
  .certificate { position: relative; width: 1200px; height: 943px; background: var(--paper); color: var(--ink); }

  /* Sidebar */
  .maxims { position: absolute; left: 84px; top: 143px; list-style: none;
    font-family: "Cutive Mono", monospace; font-size: 13.5px; color: var(--maxim-grey); letter-spacing: 0.4px; }
  .maxims li { height: 34.8px; }
  .brand { position: absolute; left: 148px; top: 588px; width: 200px; text-align: center; }
  .brand-dot { display: block; width: 84px; height: 84px; margin: 0 auto 22px; border-radius: 50%; background: var(--brand-grey); }
  .brand-name { font-family: "Montserrat", sans-serif; font-weight: 500; font-size: 22px; color: var(--brand-grey); letter-spacing: 0.5px; }
  .elements { position: absolute; left: 82px; top: 780px; display: flex; gap: 42px; }
  .element { width: 52px; height: 54px; border-radius: 14px; background: var(--icon-grey); }
  .divider { position: absolute; left: 442px; top: 110px; width: 1.6px; height: 724px; background: var(--ink); }

  /* Main panel */
  .seal { position: absolute; left: 0; top: 0; }
  .title { position: absolute; left: 0; top: 0; }
  .title text { font-family: "Cormorant Garamond", serif; font-style: italic; font-weight: 600; font-size: 54px; fill: var(--ink); letter-spacing: 1px; }

  .serif { font-family: "EB Garamond", serif; font-style: italic; }
  .date-line { position: absolute; left: 538px; top: 322px; font-size: 17px; color: var(--ink-soft); }
  .blank { display: inline-block; border-bottom: 1px solid var(--rule); vertical-align: baseline; height: 1px; }
  .graduate-line { position: absolute; left: 496px; top: 466px; width: 562px; height: 1px; background: var(--rule); }
  .declaration { position: absolute; left: 470px; top: 482px; width: 620px; text-align: center; font-size: 15.5px; line-height: 21.5px; color: var(--ink-soft); }

  .founder-name { position: absolute; left: 642px; top: 648px; width: 270px; text-align: center; font-weight: 700; font-size: 24px; color: var(--ink); }
  .founder-rule { position: absolute; left: 642px; top: 681px; width: 270px; height: 1px; background: var(--rule); }
  .founder-title { position: absolute; left: 642px; top: 690px; width: 270px; text-align: center; font-size: 15.5px; color: var(--ink-soft); }
  .signature { position: absolute; left: 726px; top: 718px; font-family: "Petit Formal Script", cursive; font-size: 24px; color: var(--ink); transform: rotate(-9deg); transform-origin: left center; }
  .established { position: absolute; left: 580px; top: 817px; width: 400px; text-align: center; font-weight: 700; font-size: 16px; color: var(--ink); }
</style>
</head>
<body>
<main class="certificate">

  <ul class="maxims">
    <li>This is Lumen Stretch</li>
    <li>Breath is primary</li>
    <li>Evolve the physical culture</li>
    <li>Bring your unique expression</li>
    <li>to the practice</li>
    <li>Take Breaks</li>
    <li>Freestyle</li>
    <li>Close your eyes</li>
    <li>Feel deeper into your body</li>
    <li>This is active meditation</li>
    <li>This is moving meditation</li>
    <li>This is modern meditation</li>
  </ul>

  <div class="brand">
    <span class="brand-dot"></span>
    <span class="brand-name">LUMEN STRETCH</span>
  </div>

  <div class="elements">
    <div class="element" role="img" aria-label="Fire icon"></div>
    <div class="element" role="img" aria-label="Water drop icon"></div>
    <div class="element" role="img" aria-label="Prayer hands icon"></div>
    <div class="element" role="img" aria-label="Leaf icon"></div>
  </div>

  <div class="divider"></div>

  <svg class="seal" width="1200" height="943" aria-hidden="true">
    <circle cx="780" cy="476" r="256" fill="none" stroke="var(--seal-grey)" stroke-width="40"/>
  </svg>

  <svg class="title" width="1200" height="260" aria-label="Certification of Completion">
    <defs><path id="title-arc" d="M 462 204 Q 777 84 1092 204"/></defs>
    <text><textPath href="#title-arc" startOffset="50%" text-anchor="middle">Certification of Completion</textPath></text>
  </svg>

  <p class="date-line serif">On this <span class="blank" style="width:88px"></span> day of <span class="blank" style="width:192px"></span> , <span class="blank" style="width:70px"></span></p>

  <div class="graduate-line"></div>

  <p class="declaration serif">
    has successfully completed the Lumen Stretch modern vinyasa yoga training,<br>
    completing two hundred hours of instruction in practice and theory.<br>
    Within the power of our institution as a certifying agent we declare <span class="blank" style="width:76px"></span>,<br>
    now, a teacher competent to share the gift of yoga with the masses in a safe and effective.
  </p>

  <p class="founder-name serif">Dennis Whitcombe</p>
  <div class="founder-rule"></div>
  <p class="founder-title serif">Lumen Stretch Founder</p>
  <p class="signature">D. Whitcombe</p>

  <p class="established serif">Lumen Stretch ~ Established 2017</p>

</main>
</body>
</html>
```